New doctor needs elegant, whimsical Business Card Design

CHALLENGE: how to highlight gynaecological service (use of abstract cervix in logo?) in NON-VULGAR way + project an elegant, professional tone?

We need a business card design (incl logo) for a gynaecologist who is starting his private practice. The main area of service will be colposcopy - a diagnostic procedure using a microscope to look at the tissues of the cervix for any potentially cancerous cells.

STYLE: Classic, elegant, timeless look. Fairly simple, not too cluttered. Logo NOT to overpower name. Want to project a professional but approachable image - "gentleman". Not too "corporate" - whimsical, without becoming feminine.

COLOUR: soft colours - no clashing primary colours, nothing too "brash" or commercial.
White background/black lettering + 1 colour accent, pattern repeated throughout card, in both logo & text (refer to "mock-up example" image file)
The colour accent should be BLUE: a serene/calm but confident shade: eg. strong pastel blue, dark baby blue (NOT royal blue, navy, turquoise, aquamarine, etc)

TEXT: have a calligraphy feel (but not too fancy as to be difficult to read at a glance) or more italics/rounded edges kind of font (refer to refer to "mock-up example" image file)
- Contrast between NAME in more italic font Vs. rest of text in "straight" print (or vice versa)

LOGO:
1) something very similar to "The Wren Trust" logo (ref image attached) - an abstract, black line drawing of a woman's figure, with a single, coloured symbol. No detail in line drawing - NO head or arms - don't want it to be obviously women's figure - want it very stylised, abstract, fluid lines.

* The Wren Trust used a heart but we would like to use an another symbol in BLUE - maybe an abstract of a cervix? eg. the "triangle" shape symbol (see the image file of the Silver Thread Wellness Initiative - the symbol in the middle of the flower) OR the "donut" representation of the cervix (see notes below)

BUT - don't want the symbol exactly over the groin area, otherwise looks vulgar. Don't want it to look like bikini or genitals! Symbol should be incorporated into line drawing but NOT drawing direct attention to the groin. Maybe displaced to one side? Or further up the body? Open to your ideas

2) We are also open to any other ideas you may have, of stylistic/abstract designs based on:
- the image of a cervix (looks very similar to a pink donut - usually shown in medical shorthand as a tiny circle in the middle of a bigger circle.)
- the cervix with some cells within ? Some stylised version of cancer cells?
(please see attached selection of images for reference/inspiration)

2 main audiences: women (18 - 70) concerned about abnormal PAP smear, other gynae-issues, 2) GP's referring their patients to a gynae-specialist

Medical

• ONE side only - Reverse of business card must be kept blank for "Appointments" notes.

• NO "retro" American feel - nor anything 60's or 70's kind of feel. Don't want fonts that look too commercial or industrial/harsh.

Logo: NO obvious silhouettes/profiles of women (abstract is OK but not detail), NO female reproductive system (2 ovaries & uterus), no female symbol - as these are the usual cliches for gynaecologists.

DON'T want the symbol exactly over the groin area, otherwise looks vulgar. Don't want it to look like bikini or genitals! Symbol should be incorporated into line drawing but NOT drawing direct attention to the groin. Maybe displaced to one side? Or further up the body? Open to your ideas

```html
<!DOCTYPE html>
<html lang="en">
<head>
<meta charset="utf-8">
<title>Dr. Neil Harper – Business Card</title>
<link rel="stylesheet" href="https://fonts.googleapis.com/css2?family=Yellowtail&family=Damion&family=Questrial&display=block">
<style>
  :root {
    --paper: #ffffff;
    --ink: #0d0d0d;
    --accent: #5eaef2;
    --accent-soft: #b9dbf7;
    --mute: #c9c9c9;
  }
  * { margin: 0; padding: 0; box-sizing: border-box; }
  html, body {
    width: 1200px; height: 697px; overflow: hidden; background: var(--paper);
  }
  .card {
    position: relative; width: 1200px; height: 697px; overflow: hidden;
    background: var(--paper);
    font-family: "Questrial", sans-serif; color: var(--ink);
  }
  .brand-mark {
    position: absolute; left: 30px; top: 240px;
    display: flex; align-items: center; gap: 8px;
    font-size: 19px; color: var(--mute); white-space: nowrap;
  }
  .brand-mark .dot {
    width: 16px; height: 16px; border-radius: 50%; background: var(--accent-soft);
  }
  .doctor-name {
    position: absolute; left: 216px; top: 178px;
    font-size: 90px; font-weight: 400; line-height: 1; letter-spacing: 0.5px;
    white-space: nowrap;
  }
  .specialty {
    position: absolute; left: 220px; top: 280px; width: 764px; height: 60px;
    display: flex; align-items: center; justify-content: space-between;
  }
  .specialty .rule { height: 4px; width: 48px; background: var(--ink); }
  .specialty .label {
    font-family: "Yellowtail", "Damion", cursive; font-style: italic;
    font-size: 58px; color: var(--accent); white-space: nowrap; line-height: 1;
  }
  .credentials {
    position: absolute; left: 221px; top: 374px;
    font-size: 35px; white-space: nowrap; line-height: 1;
  }
  .address {
    position: absolute; left: 49px; top: 534px;
    font-size: 35px; line-height: 40px; font-style: normal; white-space: nowrap;
  }
  .contacts {
    position: absolute; left: 738px; top: 497px; list-style: none;
    font-size: 32px; line-height: 1;
  }
  .contacts li { display: flex; align-items: center; gap: 12px; height: 51px; white-space: nowrap; }
  .contacts .badge {
    width: 40px; height: 40px; border-radius: 50%; background: var(--accent);
    color: var(--paper); font-size: 28px; flex: none;
    display: flex; align-items: center; justify-content: center;
  }
</style>
</head>
<body>
  <main class="card">
    <div class="brand-mark"><span class="dot"></span><span>Neil Harper</span></div>

    <h1 class="doctor-name">DR. NEIL HARPER</h1>

    <div class="specialty">
      <span class="rule"></span>
      <span class="label">Gynaecologist - Colposcopy</span>
      <span class="rule"></span>
    </div>

    <p class="credentials">BM BCh, MA (Oxon), Dip Obs, FRANZCOG, MD</p>

    <address class="address">
      Suite 12, Kingsbury Medical Centre<br>
      40 Lindell Ave, Claremont, WA 6010
    </address>

    <ul class="contacts">
      <li><span class="badge">T</span><span>+61 8 63550142</span></li>
      <li><span class="badge">F</span><span>+61 8 63550178</span></li>
      <li><span class="badge">E</span><span>admin@harpergyn.com.au</span></li>
    </ul>
  </main>
</body>
</html>
```